Tech business card design

We need an amazing business card design for our new business 'Vantry' a marketing tech startup based in Sydney, Australia. We provide an online marketplace for businesses to search and buy advertising media, connect with service providers and learn more about marketing. We wish to communicate 'cool tech', reliability and professionalism and design based around our logo.

Target Market(s)

Business Owners

Contact Information for Business Card

Name
Position
Email Address
Website
Phone Number

Font styles to use
Other font styles liked:
• Avenir & Avenir Next

Colors

Designer to choose colors to be used in the design.

```html
<!DOCTYPE html>
<html lang="en">
<head>
<meta charset="utf-8">
<title>Vantry – Business Card</title>
<link rel="stylesheet" href="https://fonts.googleapis.com/css2?family=Nunito+Sans:wght@400;700;800;900&display=swap">
<style>
  :root {
    --page-bg: #efefef;
    --navy-deep: #12133a;
    --navy: #1b2448;
    --teal: #6ab3c2;
    --teal-text: #5ea9b8;
    --white: #ffffff;
    --ghost-light: #e3e4e9;
    --ghost-dark: rgba(14, 20, 56, 0.32);
    --ink: #3a3a3f;
    --rule: #2a2c4a;
  }
  * { margin: 0; padding: 0; box-sizing: border-box; }
  html, body {
    width: 1200px;
    height: 900px;
    overflow: hidden;
    background: var(--page-bg);
    font-family: "Nunito Sans", "Avenir Next", Avenir, sans-serif;
  }
  .card {
    position: absolute;
    overflow: hidden;
  }
  .card-front {
    left: 301px; top: 84px;
    width: 599px; height: 342px;
    background: linear-gradient(225deg, var(--teal) 0%, #3d6680 30%, var(--navy) 62%, var(--navy-deep) 100%);
  }
  .card-back {
    left: 302px; top: 473px;
    width: 603px; height: 344px;
    background: var(--white);
  }
  .ghost-word {
    position: absolute;
    font-weight: 900;
    font-size: 230px;
    line-height: 1;
    letter-spacing: -6px;
    white-space: nowrap;
  }
  .card-front .ghost-word { left: 22px; top: -62px; color: var(--ghost-dark); }
  .card-back .ghost-word { left: 22px; top: -64px; color: var(--ghost-light); }
  .wordmark {
    position: absolute;
    font-weight: 900;
    line-height: 1;
    letter-spacing: -2px;
    white-space: nowrap;
  }
  .card-front .wordmark {
    left: 0; width: 100%; top: 114px;
    text-align: center;
    font-size: 92px;
    color: var(--white);
  }
  .card-back .wordmark {
    left: 40px; top: 30px;
    font-size: 82px;
    color: var(--navy-deep);
  }
  .front-url {
    position: absolute;
    left: 0; width: 100%; top: 203px;
    text-align: center;
    font-size: 15px;
    color: var(--white);
    letter-spacing: 0.3px;
  }
  .holder {
    position: absolute;
    right: 43px; top: 144px;
    text-align: right;
  }
  .holder-name {
    font-weight: 800;
    font-size: 20px;
    color: var(--navy-deep);
    letter-spacing: 0.5px;
    line-height: 1.1;
  }
  .holder-role {
    font-size: 14px;
    color: var(--teal-text);
    letter-spacing: 0.3px;
    margin-top: 2px;
  }
  .divider {
    position: absolute;
    left: 41px; top: 203px;
    width: 518px; height: 1.5px;
    background: var(--rule);
  }
  .contact-list {
    position: absolute;
    left: 39px; top: 224px;
    list-style: none;
  }
  .contact-list li {
    display: flex;
    align-items: center;
    height: 25.5px;
    font-size: 16px;
    color: var(--ink);
  }
  .contact-list svg {
    width: 16px; height: 16px;
    margin-right: 10px;
    fill: var(--navy-deep);
    flex: none;
  }
</style>
</head>
<body>
  <section class="card card-front">
    <div class="ghost-word" aria-hidden="true">vantry</div>
    <div class="wordmark">vantry</div>
    <div class="front-url">www.vantrymedia.com.au</div>
  </section>

  <section class="card card-back">
    <div class="ghost-word" aria-hidden="true">vantry</div>
    <div class="wordmark">vantry</div>
    <div class="holder">
      <div class="holder-name">MARCUS DALE</div>
      <div class="holder-role">Founder | Director</div>
    </div>
    <div class="divider"></div>
    <ul class="contact-list">
      <li>
        <svg viewBox="0 0 16 16" aria-hidden="true"><path d="M4 0h8a1.5 1.5 0 0 1 1.5 1.5v13A1.5 1.5 0 0 1 12 16H4a1.5 1.5 0 0 1-1.5-1.5v-13A1.5 1.5 0 0 1 4 0zm0.5 2v10.5h7V2zM8 13.4a.9.9 0 1 0 0 1.8.9.9 0 0 0 0-1.8z"/></svg>
        +61 (0)412 555 208
      </li>
      <li>
        <svg viewBox="0 0 16 16" aria-hidden="true"><path d="M0 3h16v1.2L8 9 0 4.2zM0 5.6l8 4.8 8-4.8V13H0z"/></svg>
        marcus@vantrymedia.com.au
      </li>
      <li>
        <svg viewBox="0 0 16 16" aria-hidden="true"><circle cx="8" cy="8" r="7.5"/><path d="M4 4.5c1.5-.5 2.5.5 2 1.5S4.5 7.5 5.5 9s0 3-1 3.5M10 2.5c-.5 1 .5 2 1.5 2s1.5 1.5.5 2.5-2 .5-2 2 1 2 2 2.5" fill="none" stroke="#fff" stroke-width="1.2"/></svg>
        www.vantrymedia.com.au
      </li>
    </ul>
  </section>
</body>
</html>
```